Startup Drone Platform Company business card

We are needing a business card design for our employees. We are a startup drone platform. We are looking for a business card that has our logo on one side, with the employee/company details on the opposite side. We are looking for something that is very eye catching, modern, and bold.

Target Market(s)

This will target both drone pilots and drone businesses, along with all the industries that could utilize drone services (aerial video, aerial photos, inspections, 3d mapping, etc).

Industry/Entity Type

Business

```html
<!DOCTYPE html>
<html lang="en">
<head>
<meta charset="utf-8">
<title>Skyward Lift – Business Card</title>
<link href="https://fonts.googleapis.com/css2?family=Roboto:wght@400;500&display=swap" rel="stylesheet">
<style>
  :root {
    --stage: #34302d;
    --ink: #050505;
    --teal: #3fbdc9;
    --white: #ffffff;
    --back: #242424;
    --text-dark: #111111;
  }
  * { box-sizing: border-box; margin: 0; padding: 0; }
  html, body { width: 1200px; height: 934px; overflow: hidden; }
  body {
    background: var(--stage);
    font-family: "Roboto", Arial, sans-serif;
    position: relative;
  }
  .card {
    position: absolute;
    left: 284px;
    width: 634px;
    height: 362px;
    border-radius: 24px;
    overflow: hidden;
  }
  .card-front { top: 76px; background: var(--teal); }
  .card-back { top: 494px; background: var(--back); }

  .front-header {
    position: absolute; left: 0; top: 0; width: 100%; height: 162px;
    background: var(--ink);
  }
  .header-notch {
    position: absolute; left: 36px; top: 161px;
  }
  .brand-name {
    position: absolute; left: 0; right: 0; top: 56px;
    text-align: center;
    color: var(--white);
    font-weight: 500;
    font-size: 34px;
    letter-spacing: 0.42em;
    padding-left: 0.42em;
  }
  .holder {
    position: absolute; left: 52px; top: 206px;
    display: flex; align-items: baseline;
    color: var(--text-dark);
  }
  .holder-name { font-size: 25px; font-weight: 400; }
  .holder-divider {
    display: inline-block; width: 2px; height: 24px; background: var(--text-dark);
    margin: 0 13px; align-self: center;
  }
  .holder-title { font-size: 17px; }
  .contact-list {
    position: absolute; left: 50px; top: 327px; list-style: none;
  }
  .contact-list { top: 253px; }
  .contact-item {
    display: flex; align-items: center; height: 21px;
    font-size: 17px; color: var(--text-dark);
  }
  .contact-icon { width: 16px; height: 16px; margin-right: 10px; flex: none; }

  .back-mark {
    position: absolute; left: 50%; top: 110px; transform: translateX(-50%);
  }
  .back-name {
    position: absolute; left: 0; right: 0; top: 230px;
    text-align: center; color: var(--white);
    font-weight: 500; font-size: 22px;
    letter-spacing: 0.5em; padding-left: 0.5em;
    line-height: 30px;
  }
  .back-web {
    position: absolute; left: 0; right: 0; top: 310px;
    text-align: center; color: var(--white); font-size: 15px; letter-spacing: 0.02em;
  }
</style>
</head>
<body>
  <section class="card card-front">
    <div class="front-header">
      <div class="brand-name">SKYWARD LIFT</div>
    </div>
    <svg class="header-notch" width="46" height="24" viewBox="0 0 46 24"><polygon points="0,0 46,0 23,24" fill="var(--ink)"/></svg>

    <div class="holder">
      <span class="holder-name">Dana Whitlock</span>
      <span class="holder-divider"></span>
      <span class="holder-title">Founder/CEO</span>
    </div>

    <ul class="contact-list">
      <li class="contact-item">
        <svg class="contact-icon" viewBox="0 0 16 16"><rect x="4" y="1" width="8" height="14" rx="1.5" fill="none" stroke="#111" stroke-width="1.6"/><line x1="7" y1="12.5" x2="9" y2="12.5" stroke="#111" stroke-width="1.4"/></svg>
        877-555-0142
      </li>
      <li class="contact-item">
        <svg class="contact-icon" viewBox="0 0 16 16"><rect x="1" y="4" width="14" height="9" fill="#111"/><polyline points="1,4 8,9.5 15,4" fill="none" stroke="#3fbdc9" stroke-width="1.2"/></svg>
        dana.whitlock@skywardlift.com
      </li>
      <li class="contact-item">
        <svg class="contact-icon" viewBox="0 0 16 16"><circle cx="8" cy="8" r="6.5" fill="none" stroke="#111" stroke-width="1.6"/><path d="M1.5 8h13M8 1.5c-3 3.5-3 9.5 0 13M8 1.5c3 3.5 3 9.5 0 13" fill="none" stroke="#111" stroke-width="1.2"/></svg>
        www.SKYWARDLIFT.com
      </li>
      <li class="contact-item">
        <svg class="contact-icon" viewBox="0 0 16 16"><polygon points="8,1.5 15.5,8 13,8 13,14.5 9.5,14.5 9.5,10 6.5,10 6.5,14.5 3,14.5 3,8 0.5,8" fill="#111"/></svg>
        418 NW Orchard Park Rd. Ste 210, Cedar Falls, MO 64010
      </li>
    </ul>
  </section>

  <section class="card card-back">
    <svg class="back-mark" width="90" height="90" viewBox="0 0 90 90" aria-hidden="true"><circle cx="45" cy="45" r="40" fill="none" stroke="var(--teal)" stroke-width="4"/></svg>
    <div class="back-name">SKYWARD<br>LIFT</div>
    <div class="back-web">www.SKYWARDLIFT.com</div>
  </section>
</body>
</html>
```